Online Psychology Practice needs business cards.

Online Psychology service needs business cards. Have own logo- please see uploaded. I have other file formats if you need (not sure one needed?)

Details for Business Card:
Helena Marchetti
Clinical Psychologist BPsych, BPsych (Hons), MPsych (Clin), MAPS
T: 0439627015 | F: 08 73615204
E: hello@brightwatertelehealthcounselling.com.au
W: brightwatertelehealthcounselling.com.au

Industry/Entity Type

Health

Contact Information for Business Card

Logo plus details above (couldn't write in this section)

```html
<!DOCTYPE html>
<html lang="en">
<head>
<meta charset="utf-8">
<title>Brightwater Telehealth Counselling – Business Cards</title>
<link rel="stylesheet" href="https://fonts.googleapis.com/css2?family=Cinzel:wght@700&family=Roboto+Condensed:wght@400&display=swap">
<style>
  :root {
    --bg: #242424;
    --card-white: #ffffff;
    --navy: #1a5a86;
    --teal: #1a8aa6;
    --ink: #3a3a3a;
    --rule: #cfcfcf;
    --grad-top: #175c87;
    --grad-bottom: #0e8ba6;
    --shadow: rgba(0, 0, 0, 0.55);
  }
  html, body {
    margin: 0;
    padding: 0;
    width: 1065px;
    height: 1200px;
    overflow: hidden;
    background: var(--bg);
  }
  .canvas {
    position: relative;
    width: 1065px;
    height: 1200px;
  }
  .card {
    position: absolute;
    width: 582px;
    height: 363px;
    box-shadow: 3px 3px 4px var(--shadow);
    overflow: hidden;
  }
  .card--front {
    left: 292px;
    top: 218px;
    background: var(--card-white);
    border-radius: 0 181px 181px 0;
  }
  .card--back {
    left: 263px;
    top: 623px;
    background: linear-gradient(180deg, var(--grad-top), var(--grad-bottom));
    border-radius: 181px 0 0 181px;
  }

  /* Front: brand block */
  .brand-front {
    position: absolute;
    left: 28px;
    top: 120px;
    width: 170px;
    display: flex;
    align-items: center;
    gap: 10px;
  }
  .brand-front__dot {
    flex: none;
    width: 22px;
    height: 22px;
    border-radius: 50%;
    background: var(--teal);
  }
  .brand-front__name {
    font-family: "Roboto Condensed", sans-serif;
    font-weight: 400;
    font-size: 19px;
    line-height: 1.15;
    color: var(--navy);
    text-transform: uppercase;
    letter-spacing: 1px;
  }
  .divider {
    position: absolute;
    left: 213px;
    top: 97px;
    width: 1px;
    height: 166px;
    background: var(--rule);
  }

  /* Front: person details */
  .person {
    position: absolute;
    left: 238px;
    top: 96px;
  }
  .person__name {
    margin: 0;
    font-family: "Cinzel", serif;
    font-weight: 700;
    font-size: 22px;
    line-height: 1;
    color: var(--navy);
    letter-spacing: 0.3px;
  }
  .person__title {
    margin: 8px 0 0;
    font-family: "Roboto Condensed", sans-serif;
    font-size: 14.5px;
    line-height: 19px;
    color: var(--ink);
  }
  .contacts {
    list-style: none;
    margin: 20px 0 0;
    padding: 0;
    font-family: "Roboto Condensed", sans-serif;
    font-size: 14.5px;
    color: var(--ink);
  }
  .contacts__item {
    display: flex;
    align-items: center;
    gap: 6px;
    height: 20.3px;
  }
  .contacts__icon {
    width: 14px;
    height: 14px;
    flex: none;
    fill: var(--navy);
  }

  /* Back: brand block */
  .brand-back__mark {
    position: absolute;
    left: 244px;
    top: 70px;
    width: 92px;
    height: 92px;
    border-radius: 50%;
    background: var(--card-white);
  }
  .brand-back__name {
    position: absolute;
    left: 0;
    right: 0;
    top: 220px;
    margin: 0;
    text-align: center;
    font-family: "Roboto Condensed", sans-serif;
    font-weight: 400;
    font-size: 24px;
    line-height: 30px;
    letter-spacing: 4px;
    text-transform: uppercase;
    color: var(--card-white);
  }
</style>
</head>
<body>
<main class="canvas">

  <section class="card card--front" aria-label="Business card front">
    <div class="brand-front">
      <span class="brand-front__dot"></span>
      <span class="brand-front__name">Brightwater<br>Telehealth<br>Counselling</span>
    </div>
    <div class="divider"></div>
    <div class="person">
      <h1 class="person__name">HELENA MARCHETTI</h1>
      <p class="person__title">Clinical Psychologist BPsych<br>BPsych (Hons), MPsych (Clin), MAPS</p>
      <ul class="contacts">
        <li class="contacts__item">
          <svg class="contacts__icon" viewBox="0 0 16 16" aria-hidden="true"><path d="M3.5 1.5l2.3 2.6-1.3 1.9c.8 1.9 2.5 3.6 4.4 4.4l1.9-1.3 2.6 2.3-1.6 2.2C6.8 13.2 2.8 9.2 1.4 3.1z"/><path d="M9 2a5 5 0 0 1 5 5h-1.2A3.8 3.8 0 0 0 9 3.2zm0 2.4A2.6 2.6 0 0 1 11.6 7h-1.2A1.4 1.4 0 0 0 9 5.6z"/></svg>
          <span>0439627015</span>
        </li>
        <li class="contacts__item">
          <svg class="contacts__icon" viewBox="0 0 16 16" aria-hidden="true"><rect x="4" y="1" width="8" height="4"/><path d="M1 6h14v6h-2.5v-2h-9v2H1z"/><rect x="4.5" y="11" width="7" height="4"/></svg>
          <span>08 73615204</span>
        </li>
        <li class="contacts__item">
          <svg class="contacts__icon" viewBox="0 0 16 16" aria-hidden="true"><path d="M1 3h14v10H1zm1.5 1.3v.3L8 9l5.5-4.4v-.3z"/></svg>
          <span>hello@brightwatertelehealthcounselling.com.au</span>
        </li>
        <li class="contacts__item">
          <svg class="contacts__icon" viewBox="0 0 16 16" aria-hidden="true"><path fill-rule="evenodd" d="M8 1a7 7 0 1 0 0 14A7 7 0 0 0 8 1zm-.6 1.3C6.3 3.4 5.7 5 5.6 7.4H2.4a5.7 5.7 0 0 1 5-5.1zm1.2 0a5.7 5.7 0 0 1 5 5.1h-3.2c-.1-2.4-.7-4-1.8-5.1zM6.8 7.4c.1-2.1.6-3.6 1.2-4.5.6.9 1.1 2.4 1.2 4.5zm-4.4 1.2h3.2c.1 2.4.7 4 1.8 5.1a5.7 5.7 0 0 1-5-5.1zm4.4 0h2.4c-.1 2.1-.6 3.6-1.2 4.5-.6-.9-1.1-2.4-1.2-4.5zm3.6 0h3.2a5.7 5.7 0 0 1-5 5.1c1.1-1.1 1.7-2.7 1.8-5.1z"/></svg>
          <span>brightwatertelehealthcounselling.com.au</span>
        </li>
      </ul>
    </div>
  </section>

  <section class="card card--back" aria-label="Business card back">
    <span class="brand-back__mark"></span>
    <p class="brand-back__name">Brightwater<br>Telehealth Counselling</p>
  </section>

</main>
</body>
</html>
```